Non-Alcoholic Beverage Industry Grant Recipient Signage (Recycling Focus)

Marrowfield Urbanworks, a non-profit organization in Youngstown, OH, recently received a grant through the Plainsridge Drink Council (us) and the National Refreshment Trust for a Thriving Nation. This grant will go towards the installation of garbage/recycling receptacles throughout the downtown area including the Calder Ridge College campus and adjacent neighborhoods and gateways.
Specifically, this will:
a. Replace garbage receptacles with ones compatible with new Ploverbin cigarette butt receptacles previously purchased; this will reduce cigarette litter as well as improve cleanliness of downtown area;
b. Convert current trash receptacles into recycling bins. This would allow Youngstown to start a new downtown recycling program.
We are responsible for designing a 12” by 18” sign that reflects our involvement in the project and encourages recycling. We request that you do not copy/paste the above, rather come up with a creative, unique design that reflects the goal of recycling.
Plainsridge Drink Council
plainsdrinkcouncil.example
Progress Organically
https://www.progressorganically.example/plastic/
National Refreshment Trust for a Thriving Nation http://www.refreshmenttrust.example/
Marrowfield Urbanworks
http://www.marrowfieldurbanworks.example/
The signage must incorporate the two attached logos.
Updates
Deadline is incorrectly displaying as July 7, which was yesterday. We would like submissions by Friday, July 12 at the latest. Thank you!

```html
<!DOCTYPE html>
<html lang="en">
<head>
<meta charset="utf-8">
<title>Marrowfield Urbanworks Recycling Sign</title>
<link rel="stylesheet" href="https://fonts.googleapis.com/css2?family=Gochi+Hand&family=Montserrat:wght@700;800&display=swap">
<style>
  :root {
    --backdrop: #3a3a3c;
    --sign-white: #ffffff;
    --leaf-green: #8aab3f;
    --ink-gray: #4a4a4d;
    --icon-gray: #e4e5e7;
    --sponsor-gray: #5b5d62;
  }
  * { margin: 0; padding: 0; box-sizing: border-box; }
  html, body {
    width: 1200px; height: 1200px; overflow: hidden;
    background: var(--backdrop);
  }
  .sign {
    position: absolute; left: 121px; top: 281px;
    width: 960px; height: 639px;
    background: var(--sign-white);
  }
  .sign-frame {
    position: absolute; left: 26px; top: 24px; right: 26px; bottom: 24px;
    border: 14px solid var(--leaf-green);
  }
  .recycle-icon { position: absolute; top: 77px; width: 132px; height: 128px; }
  .recycle-icon--left { left: 115px; }
  .recycle-icon--right { left: 696px; }
  .brand {
    position: absolute; left: 0; right: 0; top: 44px;
    display: flex; flex-direction: column; align-items: center;
  }
  .brand-mark {
    width: 130px; height: 130px; border-radius: 50%;
    background: var(--leaf-green);
  }
  .brand-name {
    margin-top: 24px;
    font-family: "Montserrat", sans-serif; font-weight: 800;
    font-size: 34px; line-height: 40px; color: var(--leaf-green); letter-spacing: 0.5px;
    white-space: nowrap;
  }
  .headline {
    position: absolute; left: 0; right: 0; top: 310px;
    text-align: center;
    font-family: "Gochi Hand", cursive; font-weight: 400;
    font-size: 62px; line-height: 64px; color: var(--ink-gray);
  }
  .sponsor-rule {
    position: absolute; left: 102px; top: 466px;
    display: flex; align-items: center; width: 878px;
  }
  .sponsor-label {
    font-family: "Montserrat", sans-serif; font-weight: 800;
    font-size: 20px; color: var(--leaf-green); white-space: nowrap;
  }
  .sponsor-line {
    margin-left: 12px; width: 572px; height: 8px;
    background: var(--leaf-green);
  }
  .sponsor {
    position: absolute; top: 514px;
    font-family: "Montserrat", sans-serif; font-weight: 700;
    font-size: 22px; line-height: 28px;
    color: var(--sponsor-gray);
    display: flex; align-items: center; gap: 12px;
    white-space: nowrap;
  }
  .sponsor--council { left: 118px; }
  .sponsor--trust { left: 380px; }
  .sponsor-mark {
    width: 42px; height: 42px; background: var(--sponsor-gray); flex: none;
  }
</style>
</head>
<body>
  <main class="sign">
    <div class="sign-frame"></div>

    <svg class="recycle-icon recycle-icon--left" viewBox="0 0 132 128" aria-hidden="true">
      <g fill="none" stroke="var(--icon-gray)" stroke-width="16" stroke-linejoin="round">
        <path d="M50 22 L82 22 L98 50"/>
        <path d="M110 74 L94 104 L62 104"/>
        <path d="M38 104 L22 76 L38 48"/>
      </g>
      <g fill="var(--icon-gray)">
        <path d="M84 42 L112 40 L100 66 Z"/>
        <path d="M66 90 L50 114 L66 120 Z"/>
        <path d="M26 38 L54 36 L40 62 Z"/>
      </g>
    </svg>
    <svg class="recycle-icon recycle-icon--right" viewBox="0 0 132 128" aria-hidden="true">
      <g fill="none" stroke="var(--icon-gray)" stroke-width="16" stroke-linejoin="round">
        <path d="M50 22 L82 22 L98 50"/>
        <path d="M110 74 L94 104 L62 104"/>
        <path d="M38 104 L22 76 L38 48"/>
      </g>
      <g fill="var(--icon-gray)">
        <path d="M84 42 L112 40 L100 66 Z"/>
        <path d="M66 90 L50 114 L66 120 Z"/>
        <path d="M26 38 L54 36 L40 62 Z"/>
      </g>
    </svg>

    <header class="brand">
      <div class="brand-mark"></div>
      <div class="brand-name">Marrowfield Urbanworks</div>
    </header>

    <h1 class="headline">We keep your neighborhood<br>clean and eco-friendly</h1>

    <div class="sponsor-rule">
      <span class="sponsor-label">SPONSORED BY</span>
      <span class="sponsor-line"></span>
    </div>

    <div class="sponsor sponsor--council">
      <span class="sponsor-mark"></span>
      <span>Plainsridge<br>Drink Council</span>
    </div>
    <div class="sponsor sponsor--trust">
      <span>National Refreshment Trust<br>for a Thriving Nation</span>
    </div>
  </main>
</body>
</html>
```